Booklet Design needed for Copperleaf Digital Studio

A Little bit about us:
At Copperleaf Digital Studio we offer our clients the very best in their website needs without the big price tag.

We take the hassle out of setting up a website and take care of the website design, domain registration, SEO and hosting.
We know how important it is to have a Visually Appealing website, that’s why when we are designing our websites we focus on the main things like branding, content, creativity, colors, layout, ease of use, and imagery.

Design Specifics:
I currently have two booklets that I give to my clients:
one before I start designing their site as a general information booklet
and the other one I give only once I complete their site - which is about how to use my editor.

I want to jazz these two booklets up and bit with a modern and professional look, and I want both the booklets to have a similar design, I would also like it to be a similar look to my website, www.copperleafdigitalstudio.com.au.

Previously the budget was AUD$130. Now it is AUD$260.
This reflects your creative effort for 2 booklets.

I have uploaded the two booklets, labeled Booklet 1 (7 pages) and Booklet 2 (15 pages), inside you will find the information and images I want on each page.
The booklets also need a title page.

Thanks Designers. Will appreciate all your creative effort!

Hi Designers . i have updated the content for one of the booklets. the new file which i will upload shortly is called "New Client information Booklet content update". please use this for one of the booklets to be designed. the other booklet still needs to be done (the one with the editor information inside)Cheers Added Thursday, October 29, 2015

Target Market(s)

Small to medium Businesses

Font styles to use
Sans Serif

Colors
3176b5
5c5c5c
ffffff

Requirements
Must have
• Logo, images and content from original booklets. And the Seperate booklets for the two different booklets. Similar modern, professional design.
Nice to have
• Moder, professional design, similar look to my website. Www.copperleafdigitalstudio.com.au

```html
<!DOCTYPE html>
<html lang="en">
<head>
<meta charset="utf-8">
<title>Copperleaf Digital Studio – Client Booklet Spread</title>
<link rel="stylesheet" href="https://fonts.googleapis.com/css2?family=Roboto:ital,wght@0,400;0,500;0,700;1,400&display=swap">
<style>
  :root {
    --brand-blue: #3f9fe0;
    --brand-blue-deep: #3176b5;
    --brand-grey: #5c5c5c;
    --stripe-grey: #6d6f72;
    --paper: #ffffff;
    --backdrop: #e8e9ea;
    --ink: #1f1f1f;
  }
  * { margin: 0; padding: 0; box-sizing: border-box; }
  html, body {
    width: 1200px; height: 800px; overflow: hidden;
    background: var(--backdrop);
    font-family: "Roboto", Arial, sans-serif;
    color: var(--ink);
  }
  .spread {
    position: absolute; left: 40px; top: 40px;
    width: 1120px; height: 720px;
    display: flex;
    box-shadow: 0 6px 24px rgba(0,0,0,.18);
  }
  .page {
    position: relative; width: 560px; height: 720px;
    background: var(--paper); overflow: hidden;
  }
  .page--left { box-shadow: inset -18px 0 24px -20px rgba(0,0,0,.25); }
  .page--right { box-shadow: inset 18px 0 24px -20px rgba(0,0,0,.25); }
  .shapes { position: absolute; inset: 0; width: 560px; height: 720px; }

  .photo { position: absolute; }
  .photo--devices {
    left: 0; top: 40px; width: 560px; height: 270px;
    background: radial-gradient(ellipse at 60% 45%, #ffffff 0%, #e4ebf1 45%, #b9c7d3 100%);
    clip-path: polygon(0 100%, 0 92%, 430px 0, 560px 0, 560px 100%);
  }
  .photo--screens {
    left: 0; top: 30px; width: 560px; height: 300px;
    background: radial-gradient(ellipse at 45% 45%, #e9f2fa 0%, #8fb0cc 35%, #3a5878 75%, #1e3148 100%);
    clip-path: polygon(0 0, 100% 0, 100% 82%, 0 100%);
  }

  .intro-note {
    position: absolute; left: 28px; top: 26px; width: 250px;
    color: var(--paper); font-size: 11px; line-height: 1.35; font-style: italic;
  }
  .intro-note p + p { margin-top: 8px; }

  .section-title {
    font-weight: 500; font-size: 27px; line-height: 1.15; color: var(--brand-grey);
  }
  .section-title .accent { color: var(--brand-blue); }
  .section-title .accent-line { display: block; color: var(--brand-blue); }

  .our-will { position: absolute; left: 80px; top: 372px; width: 430px; }
  .why-us { position: absolute; left: 60px; top: 388px; width: 450px; }
  .body-copy { font-size: 11.5px; line-height: 1.35; margin-top: 18px; }
  .body-copy p + p { margin-top: 10px; }
  .values { list-style: none; margin: 14px 0 12px; }
  .values li { position: relative; padding-left: 16px; }
  .values li::before { content: "•"; position: absolute; left: 0; }
</style>
</head>
<body>
<main class="spread">
  <section class="page page--left">
    <div class="photo photo--devices" role="img" aria-label="Photo of a desktop monitor, tablet and phone showing website layouts"></div>
    <svg class="shapes" viewBox="0 0 560 720" aria-hidden="true">
      <polygon points="0,0 380,0 0,250" fill="var(--brand-blue)"/>
      <polygon points="0,250 380,0 430,0 0,290" fill="var(--stripe-grey)"/>
      <polygon points="0,300 80,300 0,370" fill="var(--stripe-grey)"/>
      <polygon points="0,300 140,300 0,330" fill="var(--brand-blue)"/>
    </svg>
    <div class="intro-note">
      <p>Lorem Ipsum is simply dummy text of the printing and typesetting industry.</p>
      <p>Lorem Ipsum has been the industry's standard dummy text ever since the 1500s, when an unknown printer took a galley of type.</p>
    </div>
    <article class="our-will">
      <h2 class="section-title">Our <span class="accent">Will</span></h2>
      <div class="body-copy">
        <p>We will collaborate on website projects with our clients and cultivate a friendly working relationship by:</p>
        <ul class="values">
          <li>Listen to your needs</li>
          <li>Value your input</li>
          <li>Being committed to developing a website that is tailored to your needs</li>
          <li>Being prompt, reliable &amp; honest.</li>
        </ul>
        <p>We know how important it is to have a Visually Appealing website, that's why when we are designing our website's we focus on the main things like branding, content, creativity, colors, layout, ease of use, and imagery.</p>
      </div>
    </article>
  </section>

  <section class="page page--right">
    <div class="photo photo--screens" role="img" aria-label="Photo of a hand reaching toward a stream of floating screens"></div>
    <svg class="shapes" viewBox="0 0 560 720" aria-hidden="true">
      <polygon points="0,330 560,276 560,286 120,350 0,352" fill="var(--brand-blue)"/>
      <polygon points="0,352 120,350 60,362 0,362" fill="var(--stripe-grey)"/>
      <polygon points="400,720 560,630 560,720" fill="var(--brand-blue)"/>
    </svg>
    <article class="why-us">
      <h2 class="section-title">Why We Are Your <span class="accent-line">Number One Choice</span></h2>
      <div class="body-copy">
        <p>Because we don't have contracts or ongoing fees.<br>
        We only charge a one off website design and setup fee, additional fees that will be charged is a website hosting &amp; domain registration fee (charged every one or two years), general maintenance fee if required or if you would like extra features added to your site.<br>
        Once you pay for your site it's all yours! We don't hold copyright or royalties over any content on your website.<br>
        Clients will also receive a package that includes how to operate the editing platform, with statistics upon how well their new website is going, and premium support.</p>
      </div>
    </article>
  </section>
</main>
</body>
</html>
```